GuardLume website design #1 alarm company in Arizona and California

Alarm company, home security, home protection, video, home automation, smart home, we protect family we the highest quality security products in the market with 24 hour montrioning, also allow family's to control their whole house by being everywhere in the world.

In short, we’re professional, experienced and have the necessary know-how to optimally secure your home or business. Add those skills with our commitment to service and saving you money, and you can’t go wrong trusting

Looking to have a website for current customers and future customers and current employees and future employees to go to. Target current markets listed below get a lot of leads of the website.

Target Market(s)

Arizona and California, Phoenix, Mesa,Gilbert, casa grande, Arizona city, Glendale, peoria, Goodyear, Scottsdale, fountain hills, apache junction, Tempe, surprise, anthem, buckeye, Tucson, Northern California, Modesto, Fresno, Stockton, San Jose, Manteca, Tracy, Sacramento, concord, Southern California, San Bernardino, riverside, Anaheim, Los Angeles, palm desert, Bakersfield

Industry/Entity Type

Security

Coding

Coded - Design and coding required

Number of Pages Required

5+ page

Font styles to use
Sans Serif

Colors
ec1f27
f59296
ffffff
000000
b2b2b2
cacaca
fbd4d5

Requirements
Must have
• A place where a customer can put in the info to get a system(get a free quote),a link to all of my socal media sites, a work for us page, about us page, equipment page, packages page, security page, cameras page, smart home page, support page(FAQ http://www.brightvalehome.example/faq)somthing like the alomost every answer is right. Partners page.
Nice to have
• Quorlan.example, very nicely done make it look nice like this.
• Brightvalehome.example
• Pemby.example
• Tulsix.example
• Sentravox9.example
• Wexmoresecurity.example
• These are all my favorite sites would love for it to look like this sites.
Should not have
• Need to be clean cut and sharp looking, no unnecessary stuff in it.

```html
<!DOCTYPE html>
<html lang="en">
<head>
<meta charset="utf-8">
<title>GuardLume – Home Automation and Security</title>
<link href="https://fonts.googleapis.com/css2?family=Open+Sans:ital,wght@0,400;0,600;0,700;1,400&family=PT+Sans:wght@400;700&display=swap" rel="stylesheet">
<style>
:root{
  --red:#ec1f27;
  --pink:#f59296;
  --blush:#fbd4d5;
  --white:#ffffff;
  --black:#000000;
  --ink:#333333;
  --grey:#b2b2b2;
  --grey-light:#cacaca;
  --text-soft:#555555;
}
*{box-sizing:border-box;margin:0;padding:0}
html,body{width:836px;height:1200px;overflow:hidden;background:var(--white)}
body{position:relative;font-family:"Open Sans",sans-serif;color:var(--ink)}
.abs{position:absolute}

/* header */
.site-header{left:0;top:0;width:836px;height:53px;background:var(--white);border-bottom:1px solid #e4e4e4}
.brand{left:54px;top:14px;display:flex;align-items:center;gap:6px;font-family:"Open Sans",sans-serif;font-weight:700;font-size:15px;color:var(--red);letter-spacing:.2px}
.brand-mark{width:10px;height:10px;background:var(--red)}
.main-nav{left:0;top:0;height:53px}
.nav-link{position:absolute;top:19px;font-size:8px;color:var(--ink);text-decoration:none;white-space:nowrap}
.nav-link.active{color:var(--red)}
.nav-active-bar{left:368px;top:0;width:25px;height:3px;background:var(--red)}
.quote-btn{left:682px;top:17px;width:53px;height:16px;border:1.5px solid var(--red);color:var(--red);font-size:7.5px;display:flex;align-items:center;justify-content:center;text-decoration:none}

/* hero */
.hero{left:0;top:53px;width:836px;height:297px;background:linear-gradient(100deg,#f6ece4 0%,#eedfd2 35%,#d9c3b0 60%,#efe6de 100%)}
.hero-arrow{top:100px;width:38px;height:37px;background:rgba(120,120,120,.75);display:flex;align-items:center;justify-content:center}
.hero-arrow.prev{left:0}
.hero-arrow.next{left:798px}
.hero-caption{left:390px;top:165px;width:446px;height:89px;background:rgba(255,255,255,.75);padding:13px 51px 0 0;text-align:right;font-family:"PT Sans",sans-serif;font-weight:700;font-size:32px;line-height:32px;color:#3a3a3a}
.accent{color:var(--red)}

/* intro */
.intro-title{left:0;top:402px;width:836px;text-align:center;font-size:29px;line-height:46px;color:#3a3a3a;letter-spacing:-.3px}
.intro-title strong{color:var(--red);font-weight:700}
.intro-copy{left:96px;top:561px;width:644px;text-align:center;font-size:11px;line-height:16px;color:var(--text-soft)}

/* features */
.app-preview{left:55px;top:655px;width:370px;height:262px;border-radius:14px;background:linear-gradient(160deg,#f2f2f2,#d9d9d9)}
.feature{left:502px;width:298px;height:84px;padding:8px 10px 0 47px}
.feature-icon{position:absolute;left:8px;top:10px}
.feature-title{font-size:18px;line-height:22px;color:#3a3a3a}
.feature-text{margin-top:9px;font-size:9px;line-height:13px;color:var(--text-soft)}
.feature.highlight{background:var(--red)}
.feature.highlight .feature-title,.feature.highlight .feature-text{color:var(--white)}

/* footer */
.site-footer{left:0;top:985px;width:836px;height:180px;background:var(--grey-light)}
.footer-brand{left:141px;top:1024px;display:flex;align-items:center;gap:5px;font-weight:700;font-size:12px;color:var(--red)}
.footer-brand .brand-mark{width:8px;height:8px}
.footer-about{left:140px;top:1058px;width:122px;font-style:italic;font-size:7.2px;line-height:12px;color:#222}
.footer-heading{font-size:7px;font-weight:600;color:var(--white);letter-spacing:.3px}
.recent-posts{left:281px;top:1018px;width:132px}
.post-link{display:block;margin-top:0;padding:8px 0 6px;border-bottom:1px solid #555;font-size:7.2px;color:var(--red);text-decoration:none;white-space:nowrap}
.post-link:first-of-type{margin-top:4px}
.post-link:last-of-type{border-bottom:0}
.tweets{left:425px;top:1018px;width:131px}
.tweet{font-size:7.2px;line-height:12px;color:#7a7a7a}
.tweet.first{margin-top:10px;padding-bottom:12px;border-bottom:1px solid #555}
.tweet.second{margin-top:16px}
.tweet .handle{color:var(--white)}
.quote-form{left:595px;top:1018px;width:130px}
.form-label{display:block;margin-top:9px;font-size:7.2px;color:var(--red)}
.form-label:first-of-type{margin-top:10px}
.form-input{display:block;width:127px;height:10px;border:0;background:var(--white);margin-top:2px}
.send-btn{display:block;margin-top:12px;width:47px;height:16px;border:0;background:var(--red);color:var(--white);font-family:"Open Sans",sans-serif;font-size:7.5px}
.footer-bar{left:0;top:1165px;width:836px;height:35px;background:var(--grey)}
.copyright{left:138px;top:1177px;font-size:6.8px;color:#222}
.copyright .sep{color:var(--red);margin:0 4px}
.social-tip{left:588px;top:1157px;padding:2px 5px;background:#444;color:var(--white);font-size:6px}
.social-links{left:598px;top:1177px;display:flex;gap:14px}
.social-links a{font-size:6.5px;color:#444;text-decoration:none}
</style>
</head>
<body>

<header class="site-header abs">
  <a class="brand abs" href="#"><span class="brand-mark"></span>GuardLume</a>
  <nav class="main-nav abs">
    <span class="nav-active-bar abs"></span>
    <a class="nav-link active" style="left:371px" href="#">Home</a>
    <a class="nav-link" style="left:414px" href="#">About</a>
    <a class="nav-link" style="left:457px" href="#">Security</a>
    <a class="nav-link" style="left:500px" href="#">Equipment</a>
    <a class="nav-link" style="left:564px" href="#">Packages</a>
    <a class="nav-link" style="left:618px" href="#">Support</a>
  </nav>
  <a class="quote-btn abs" href="#">QUOTE</a>
</header>

<section class="hero abs" role="img" aria-label="Photo of a bright home interior with a wall-mounted security control panel, beside a ring diagram of connected devices: access, thermostats, security system, lights, door sensor, image sensor, motion sensor and window sensor, powered by Homelinq">
  <a class="hero-arrow prev abs" href="#" aria-label="Previous slide">
    <svg width="10" height="14" viewBox="0 0 10 14"><path d="M7 2 L2 7 L7 12" fill="none" stroke="#fff" stroke-width="2"/></svg>
  </a>
  <a class="hero-arrow next abs" href="#" aria-label="Next slide">
    <svg width="10" height="14" viewBox="0 0 10 14"><path d="M3 2 L8 7 L3 12" fill="none" stroke="#fff" stroke-width="2"/></svg>
  </a>
  <h1 class="hero-caption abs">Get <span class="accent">Smart</span> and Get <span class="accent">Safe</span><br>In you own <span class="accent">Home</span></h1>
</section>

<h2 class="intro-title abs">HOME <strong>AUTOMATION</strong> AND <strong>SECURITY</strong><br>INTUIATIVE <strong>INTELLIGENT</strong> DESIGN</h2>
<p class="intro-copy abs">Lorem ipsum dolor sit amet, consectetur adipiscing elit. Nullam consectetur vulputate elit ac luctus. Cras urna urna, eleifend mollis finibus in, efficitur feugiat leo. Morbi eleifend gravida iaculis.</p>

<div class="app-preview abs" role="img" aria-label="Tablet showing the Homelinq app thermostat screen for The Harlow Home, first floor at 70 degrees and second floor at 68 degrees"></div>

<article class="feature abs" style="top:648px">
  <svg class="feature-icon" width="24" height="24" viewBox="0 0 24 24"><rect x="1.5" y="1.5" width="21" height="21" fill="none" stroke="#777" stroke-width="2.5"/><path d="M9 6.5 L17 12 L9 17.5Z" fill="#777"/></svg>
  <h3 class="feature-title">Smart Tech</h3>
  <p class="feature-text">Lorem ipsum dolor sit amet, consectetur adipiscing elit.<br>Nullam consectetur vulputate el</p>
</article>
<article class="feature highlight abs" style="top:736px">
  <svg class="feature-icon" width="24" height="30" viewBox="0 0 24 30"><path d="M12 2 A9 9 0 0 1 18 18 L17 22 L7 22 L6 18 A9 9 0 0 1 12 2Z" fill="none" stroke="#fff" stroke-width="2.5"/><rect x="8" y="24" width="8" height="3" fill="#fff"/></svg>
  <h3 class="feature-title">Smart Tech</h3>
  <p class="feature-text">Lorem ipsum dolor sit amet, consectetur adipiscing elit.<br>Nullam consectetur vulputate el</p>
</article>
<article class="feature abs" style="top:844px">
  <svg class="feature-icon" width="28" height="22" viewBox="0 0 28 22"><path d="M1 1 V21 H27" fill="none" stroke="#777" stroke-width="2"/><rect x="4" y="10" width="4" height="10" fill="#777"/><rect x="10" y="5" width="4" height="15" fill="#777"/><rect x="16" y="8" width="4" height="12" fill="#777"/><rect x="22" y="12" width="4" height="8" fill="#777"/></svg>
  <h3 class="feature-title">Smart Tech</h3>
  <p class="feature-text">Lorem ipsum dolor sit amet, consectetur adipiscing elit.<br>Nullam consectetur vulputate el</p>
</article>

<footer>
  <div class="site-footer abs"></div>
  <div class="footer-brand abs"><span class="brand-mark"></span>GuardLume</div>
  <p class="footer-about abs">Lorem ipsum ex vix illud nonummy, novum tation et his. At vix scriptaset patrioque scribentur, at pro fugit erts verterem molestiae, sed et vivendo ali Lorem ipsum ex vix illud nonummy, novum tation et his. At vix scripta patrioque scribentur...</p>

  <div class="recent-posts abs">
    <h4 class="footer-heading">RECENT POSTS</h4>
    <a class="post-link" href="#">Voluptas Sadips Ipsums Dolors Untra</a>
    <a class="post-link" href="#">Fugiats Litora Ultrices Ante Auctor</a>
    <a class="post-link" href="#">Sapien Litora Dolores Ultrices</a>
    <a class="post-link" href="#">Nemis Fugiats Voluptas Dolores Uns</a>
  </div>

  <div class="tweets abs">
    <h4 class="footer-heading">CHIRPA</h4>
    <p class="tweet first">&nbsp;&nbsp;&nbsp;&nbsp;&nbsp;&nbsp;&nbsp;&nbsp;&nbsp;&nbsp;&nbsp; I What an aweosme theme! We love it, tons of options and great design, thank you! :)</p>
    <p class="tweet second"><span class="handle">@wrenfield</span> you've got to check this one out, very cool looking!</p>
  </div>

  <form class="quote-form abs">
    <h4 class="footer-heading">GET A FREE QUOTE</h4>
    <label class="form-label">Your Name (required)</label><input class="form-input" type="text">
    <label class="form-label">Your Email (required)</label><input class="form-input" type="email">
    <label class="form-label">Your Phone</label><input class="form-input" type="tel">
    <button class="send-btn" type="button">SEND</button>
  </form>

  <div class="footer-bar abs"></div>
  <p class="copyright abs">Copyright 2016 GuardLume | All Rights Reserved<span class="sep">|</span>Powered by PressCraft</p>
  <span class="social-tip abs">Friendnet</span>
  <nav class="social-links abs">
    <a href="#">Friendnet</a><a href="#">Chirpa</a><a href="#">Linkora</a><a href="#">Feed</a>
  </nav>
</footer>

</body>
</html>
```